Tamarack Hearth Partners Business Card

Looking for a new business card layout. We are a real estate firm w/ a logo, old design attached. Must keep the same elements on there, just need a fresh look and possible some foil accents. Looking for a simpler design w/ more modern style.

Target Market(s)

Real Estate clients

Industry/Entity Type

Real Estate Agent

Contact Information for Business Card

see attached

Font styles to use
Sans Serif

Requirements
Must have
• all elements on current biz card
Nice to have
• modern look, simpler than we have!
Should not have
• no serif fonts

```html
<!DOCTYPE html>
<html lang="en">
<head>
<meta charset="utf-8">
<title>Tamarack Hearth Partners Business Card</title>
<link href="https://fonts.googleapis.com/css2?family=Montserrat:wght@300;400;500;600;700&display=swap" rel="stylesheet">
<style>
  :root {
    --page-bg: #e9e9e9;
    --card-light: #f4f4f4;
    --card-grey: #dcdcdc;
    --ink: #1c1c1c;
    --accent-red: #e3262b;
    --shirt-teal: #3fc6c0;
    --hair-blonde: #d9c39a;
    --skin-warm: #e2a48c;
  }
  * { margin: 0; padding: 0; box-sizing: border-box; }
  html, body {
    width: 1200px; height: 1000px; overflow: hidden;
    background: var(--page-bg);
    font-family: "Montserrat", sans-serif;
  }
  .stage {
    width: 1200px; height: 1000px;
    display: flex; align-items: center; justify-content: center;
  }
  .business-card {
    position: relative;
    width: 980px; height: 560px;
    border-radius: 34px;
    overflow: hidden;
    background: linear-gradient(100deg, var(--card-light) 0%, #ececec 40%, var(--card-grey) 75%, #e6e6e6 100%);
    box-shadow: 0 18px 40px rgba(0,0,0,0.18);
  }
  .portrait {
    position: absolute;
    top: 0; right: 0; bottom: 0;
    width: 450px;
    background:
      radial-gradient(ellipse 30% 24% at 50% 34%, var(--skin-warm) 0%, rgba(226,164,140,0) 100%),
      radial-gradient(ellipse 50% 42% at 50% 36%, var(--hair-blonde) 0%, rgba(217,195,154,0) 100%),
      linear-gradient(180deg, #f1ede6 0%, #f1ede6 48%, var(--shirt-teal) 66%, var(--shirt-teal) 100%);
    -webkit-mask-image:
      linear-gradient(90deg, transparent 0%, #000 22%),
      linear-gradient(180deg, #000 62%, transparent 82%);
    -webkit-mask-composite: source-in;
    mask-image:
      linear-gradient(90deg, transparent 0%, #000 22%),
      linear-gradient(180deg, #000 62%, transparent 82%);
    mask-composite: intersect;
  }
  .card-content {
    position: absolute;
    left: 70px; top: 62px;
    width: 440px;
  }
  .brand-tagline {
    font-size: 30px; font-weight: 300;
    line-height: 1; letter-spacing: 0.5px;
    color: var(--accent-red);
    text-transform: uppercase;
  }
  .brand-name {
    font-size: 52px; font-weight: 600;
    line-height: 1.05; letter-spacing: -0.5px;
    color: var(--ink);
    text-transform: uppercase;
  }
  .agent-name {
    margin-top: 18px;
    font-size: 46px; font-weight: 600;
    line-height: 1.1;
    color: var(--accent-red);
    letter-spacing: -0.5px;
    text-transform: uppercase;
  }
  .agent-title {
    margin-top: 2px;
    font-size: 23px; font-weight: 500;
    color: var(--ink);
  }
  .phone-list { margin-top: 14px; list-style: none; }
  .phone-list li {
    display: flex; align-items: center; gap: 14px;
    font-size: 30px; font-weight: 600;
    color: var(--accent-red);
    line-height: 1.25;
  }
  .phone-list svg { width: 24px; height: 28px; flex: none; }
  .web-lines { margin-top: 22px; }
  .web-lines p {
    font-size: 25px; font-weight: 500;
    color: var(--ink);
    line-height: 1.45;
  }
  .web-lines .highlight { color: var(--accent-red); }
  .address {
    position: absolute;
    left: 70px; bottom: 40px;
    font-size: 25px; font-weight: 500;
    color: var(--ink);
  }
</style>
</head>
<body>
<main class="stage">
  <article class="business-card">
    <div class="portrait" role="img" aria-label="Portrait photo of the broker, smiling, in a teal blouse"></div>

    <div class="card-content">
      <p class="brand-tagline">Tamarack Hearth</p>
      <h1 class="brand-name">Partners</h1>
      <h2 class="agent-name">Dana Whitlow</h2>
      <p class="agent-title">Principal Broker</p>

      <ul class="phone-list">
        <li>
          <svg viewBox="0 0 24 28" aria-hidden="true"><rect x="5" y="2" width="14" height="24" rx="2.5" fill="none" stroke="#1c1c1c" stroke-width="2"/><line x1="10" y1="22" x2="14" y2="22" stroke="#1c1c1c" stroke-width="2"/></svg>
          555.210.4417
        </li>
        <li>
          <svg viewBox="0 0 24 28" aria-hidden="true"><path d="M2 11 C2 6 22 6 22 11 L22 13 L17 13 L17 10.5 L7 10.5 L7 13 L2 13 Z" fill="#1c1c1c"/><path d="M6 14 L18 14 L21 24 L3 24 Z" fill="#1c1c1c"/><circle cx="12" cy="19" r="2.6" fill="#f4f4f4"/></svg>
          555.318.9062
        </li>
      </ul>

      <div class="web-lines">
        <p>dana@<span class="highlight">hearthmoves</span>.com</p>
        <p>Tamarack-<span class="highlight">RealEstate</span>.com</p>
      </div>
    </div>

    <p class="address">48 Cedar Ln Ridgefield, OR 97000</p>
  </article>
</main>
</body>
</html>
```